Psychology practice - information brochure/flyer - half A4 page folded (4 sides)

We need a brochure/flyer to market our psychology service to GPs (Doctors). We need to demonstrate to the doctors that we are the right choice for their patients, and that we cover a large range of services so all of their patients needs are met. We will demonstrate this by listing our range of services and our team of psychologists. We have two locations in Sydney and offer high end services. I've attached our company logo but we remain flexible regarding the style of the brochures. I will provide more details (services, locations & psychologist credentials) once our preferred brochure design has been selected.

```html
<!DOCTYPE html>
<html lang="en">
<head>
<meta charset="utf-8">
<title>Clear Path Clinical Psychology – GP Brochure</title>
<link rel="stylesheet" href="https://fonts.googleapis.com/css2?family=Open+Sans:wght@400;600;700&display=swap">
<style>
  :root {
    --pink: #f72e9a;
    --blue: #15a9f1;
    --yellow: #fdc012;
    --green: #1ecb53;
    --white: #ffffff;
    --ink: #111111;
    --ink-soft: #454545;
    --fold: #222222;
  }
  * { box-sizing: border-box; margin: 0; padding: 0; }
  html, body { width: 1200px; height: 848px; overflow: hidden; background: var(--white); }
  body { font-family: "Open Sans", Arial, sans-serif; }
  .brochure { position: relative; width: 1200px; height: 848px; overflow: hidden; background: var(--white); }

  .side-band { position: absolute; left: 0; top: 0; width: 221px; height: 689px; background: var(--pink); }

  .header-band {
    position: absolute; left: 0; top: 48px; width: 1200px; height: 281px;
    background: var(--yellow);
    box-shadow: 0 4px 8px rgba(0,0,0,.45), 0 -3px 8px rgba(0,0,0,.3);
  }
  .header-band__inner {
    position: absolute; left: 0; top: 24px; width: 100%; height: 235px;
    background: var(--blue);
    box-shadow: 0 3px 6px rgba(0,0,0,.5), 0 -3px 6px rgba(0,0,0,.35);
  }

  .panel-box {
    position: absolute; top: 99px; height: 176px; background: var(--white);
    box-shadow: 0 2px 5px rgba(0,0,0,.35);
  }
  .locations { left: 40px; width: 538px; padding: 4px 18px; color: var(--ink); }
  .locations__title {
    text-align: center; font-size: 36px; font-weight: 600; line-height: 1.15;
    text-decoration: underline; text-underline-offset: 5px; margin-bottom: 8px;
  }
  .locations__line { font-size: 28px; font-weight: 600; line-height: 42px; white-space: nowrap; overflow: hidden; }

  .brand { left: 630px; width: 541px; display: flex; align-items: center; justify-content: center; gap: 22px; }
  .brand__mark { width: 46px; height: 46px; background: var(--yellow); flex: none; }
  .brand__name { font-size: 44px; font-weight: 400; line-height: 1.1; color: var(--ink-soft); }

  .call-out {
    position: absolute; left: 66px; top: 400px; width: 458px; height: 209px;
    background: var(--white); border: 7px solid var(--yellow);
    box-shadow: 0 2px 6px rgba(0,0,0,.4);
    display: flex; align-items: center; justify-content: center; text-align: center;
    font-size: 40px; font-weight: 600; line-height: 1.38; color: var(--ink);
  }

  .services-intro {
    position: absolute; left: 620px; top: 361px; width: 566px; text-align: center;
    font-size: 27px; font-weight: 600; line-height: 41px; color: var(--ink-soft);
  }
  .service {
    position: absolute; width: 256px; height: 63px; border-radius: 3px;
    display: flex; align-items: center; justify-content: center;
    font-size: 30px; font-weight: 600; color: var(--white);
    box-shadow: 0 2px 5px rgba(0,0,0,.35);
  }
  .service--a { left: 636px; top: 496px; background: var(--pink); }
  .service--b { left: 905px; top: 496px; background: var(--green); }
  .service--c { left: 636px; top: 571px; background: var(--blue); }
  .service--d { left: 905px; top: 571px; background: var(--yellow); }

  .footer-band {
    position: absolute; left: 0; top: 689px; width: 1200px; height: 159px; background: var(--green);
    box-shadow: 0 -3px 8px rgba(0,0,0,.35);
  }
  .contact { position: absolute; left: 0; top: 0; width: 606px; text-align: center; color: var(--white); font-weight: 600; }
  .contact__title { font-size: 36px; line-height: 1.2; text-decoration: underline; text-underline-offset: 5px; margin-top: 6px; }
  .contact__line { font-size: 31px; line-height: 46px; white-space: pre; }
  .tagline {
    position: absolute; left: 606px; top: 10px; width: 594px; text-align: center;
    font-size: 47px; font-weight: 600; line-height: 62px; color: var(--white);
  }

  .fold-line { position: absolute; left: 606px; top: 0; width: 1px; height: 848px; background: var(--fold); }
</style>
</head>
<body>
<main class="brochure">
  <div class="side-band"></div>

  <div class="header-band"><div class="header-band__inner"></div></div>

  <section class="panel-box locations">
    <h2 class="locations__title">&nbsp;Locations&nbsp;</h2>
    <p class="locations__line">Address 1 ---------------------------</p>
    <p class="locations__line">Address 2 ---------------------------</p>
  </section>

  <section class="panel-box brand">
    <span class="brand__mark"></span>
    <span class="brand__name">Clear Path<br>Clinical Psychology</span>
  </section>

  <p class="call-out">Contact us today to<br>start on the road to<br>long-lasting change!</p>

  <p class="services-intro">Offering a wide variety of services to better serve the people of Sydney such as</p>
  <div class="service service--a">Service A</div>
  <div class="service service--b">Service B</div>
  <div class="service service--c">Service C</div>
  <div class="service service--d">Service D</div>

  <footer class="footer-band">
    <div class="contact">
      <h2 class="contact__title">&nbsp;Contact&nbsp;</h2>
      <p class="contact__line">p 00 0000 0000   f 00 0000 0000</p>
      <p class="contact__line">email  abcdefg@domain.com</p>
    </div>
    <p class="tagline">Helping manage<br>and overcome</p>
  </footer>

  <div class="fold-line"></div>
</main>
</body>
</html>
```